TIDAL VERGE needs bisness cards pronto

Bisness name is "TIDAL VERGE" new bisness the bisness includes lawn mowing, garden matanace, and any jobs around the house.
I need a card that is colorful and vibrant and the bisness of lawn mowing maybe with some nature with it. It also needs my contact details"Darren Quellby mobile 0413562049 call for free quote and email norma.vance@fernmail.com.au and a catchy tag line

Industry/Entity Type

House

Requirements
Must have
• Bisness name "TIDAL VERGE"
Contact details "0413562049"
Email norma.vance@fernmail.com.au
Call for free quote

```html
<!DOCTYPE html>
<html lang="en">
<head>
<meta charset="utf-8">
<title>Tidal Verge – Business Card</title>
<link href="https://fonts.googleapis.com/css2?family=Open+Sans:wght@400;600;700&display=swap" rel="stylesheet">
<style>
  :root {
    --lime: #bcd520;
    --ink: #17181a;
    --paper: #eef0f4;
    --white: #ffffff;
    --muted: #8a8f99;
    --backdrop: #3b4352;
  }
  * { box-sizing: border-box; margin: 0; padding: 0; }
  html, body { width: 1200px; height: 900px; overflow: hidden; }
  body {
    background: var(--backdrop);
    font-family: "Open Sans", Arial, sans-serif;
    position: relative;
  }

  /* Front of card */
  .card-front {
    position: absolute;
    left: 60px; top: 278px;
    width: 620px; height: 354px;
    background: var(--paper);
    box-shadow: 0 10px 30px rgba(0,0,0,.35);
  }
  .front-band {
    position: absolute;
    left: 0; right: 0; top: 58px; height: 216px;
    background: var(--ink);
  }
  .tab-left, .tab-right {
    position: absolute;
    top: 58px; width: 24px; height: 216px;
    background: var(--lime);
  }
  .tab-left { left: 0; border-radius: 0 18px 18px 0; }
  .tab-right { right: 0; border-radius: 18px 0 0 18px; }

  .brand {
    position: absolute;
    left: 0; right: 0; top: 76px;
    display: flex; flex-direction: column; align-items: center;
  }
  .brand-dot {
    width: 52px; height: 52px; border-radius: 50%;
    background: var(--lime);
  }
  .brand-name {
    margin-top: 8px;
    color: var(--white);
    font-weight: 700; font-size: 19px; letter-spacing: .5px;
  }

  .contact-row {
    position: absolute;
    left: 44px; right: 40px; top: 178px;
    display: flex; align-items: center; justify-content: center; gap: 14px;
  }
  .person {
    font-weight: 700; font-size: 21px; color: var(--white);
  }
  .person .surname { color: var(--lime); }
  .divider { width: 2px; height: 40px; background: var(--lime); }
  .details { display: flex; flex-direction: column; gap: 3px; }
  .detail {
    display: flex; align-items: center; gap: 8px;
    color: var(--white); font-size: 14px; font-weight: 600;
  }
  .detail svg { width: 14px; height: 14px; flex: none; }
  .cta {
    position: absolute;
    left: 0; right: 0; top: 240px;
    text-align: center;
    color: var(--muted);
    font-weight: 700; font-size: 13px; letter-spacing: .3px;
  }

  /* Back of card */
  .card-back {
    position: absolute;
    left: 780px; top: 150px;
    width: 354px; height: 620px;
    background: var(--ink);
    box-shadow: 0 10px 30px rgba(0,0,0,.35);
    overflow: hidden;
  }
  .back-tab-top {
    position: absolute;
    top: 0; left: 150px; width: 170px; height: 22px;
    background: var(--lime);
    border-radius: 0 0 16px 16px;
  }
  .back-tab-bottom {
    position: absolute;
    bottom: 0; left: 30px; width: 210px; height: 28px;
    background: var(--lime);
    border-radius: 16px 16px 0 0;
  }
  .back-brand {
    position: absolute;
    left: 177px; top: 230px;
    transform: translate(-50%, -50%) rotate(-90deg);
    display: flex; align-items: center; gap: 18px;
    white-space: nowrap;
  }
  .back-brand .brand-dot { width: 60px; height: 60px; }
  .back-brand .brand-name {
    margin: 0; font-size: 26px;
  }
</style>
</head>
<body>

  <section class="card-front" aria-label="Business card front">
    <div class="front-band"></div>
    <div class="tab-left"></div>
    <div class="tab-right"></div>

    <div class="brand">
      <div class="brand-dot"></div>
      <div class="brand-name">TIDAL VERGE</div>
    </div>

    <div class="contact-row">
      <div class="person">Darren<span class="surname">Quellby</span></div>
      <div class="divider"></div>
      <div class="details">
        <div class="detail">
          <svg viewBox="0 0 14 14" aria-hidden="true"><rect x="3" y="1" width="8" height="12" rx="1.5" fill="none" stroke="var(--lime)" stroke-width="1.6"/><circle cx="7" cy="10.5" r="1" fill="var(--lime)"/></svg>
          <span>0413562049</span>
        </div>
        <div class="detail">
          <svg viewBox="0 0 14 14" aria-hidden="true"><rect x="1" y="3" width="12" height="8.5" fill="none" stroke="var(--lime)" stroke-width="1.6"/><path d="M1 3 L7 8 L13 3" fill="none" stroke="var(--lime)" stroke-width="1.6"/></svg>
          <span>norma.vance@fernmail.com.au</span>
        </div>
      </div>
    </div>

    <div class="cta">CALL FOR FREE QUOTE</div>
  </section>

  <section class="card-back" aria-label="Business card back">
    <div class="back-tab-top"></div>
    <div class="back-tab-bottom"></div>
    <div class="back-brand">
      <div class="brand-name">TIDAL VERGE</div>
      <div class="brand-dot"></div>
    </div>
  </section>

</body>
</html>
```